Wine gifting platform needs redeem/decline page

Vintaro is a wine gifting platform. Users can send wine gifts to one or many people, the recipients will then receive an email with instructions on how to redeem their wine.

This is what we need: After clicking the link in the email they will be taken to the redeem/decline page/flow where they will choose their preferred wine and enter their shipping address. I have uploaded videos of both the decline and the redeem flows.

- All existing form fields, informational text, and error messages needs to be incorporated into the new design but otherwise you have creative freedom on presentation.
- We have four gift tiers: Silver, Gold, Platinum, and Diamond. We would like the redemption page to highlight this with different colors (or something else!) that's glanceable. I have attached screenshots to highlight these.
- Our target audience is professional and corporate but we want the redemption process to feel elegant and sleek. We want it to feel like a premium experience just like the wine they'll receive.

I would prefer Sketch files over Photoshop.

Target Market(s)

Professional, corporate

Number of Pages Required

3 page

Requirements
Must have
• All fields, all 3 steps of the wizard, information, and error messages/styles in the flow videos (attached)

```html
<!DOCTYPE html>
<html lang="en">
<head>
<meta charset="utf-8">
<title>Vintaro – Choose Your Gift</title>
<link rel="stylesheet" href="https://fonts.googleapis.com/css2?family=Brygada+1918:wght@400;600;700&family=Jost:wght@300;400&display=swap">
<style>
  :root{
    --navy:#23295a;
    --navy-soft:#3a3f6b;
    --gold:#c4a36f;
    --gold-light:#d8c29c;
    --paper:#ffffff;
    --red-glass:#2b1c21;
    --white-glass:#c9a867;
    --green-glass:#2f4a33;
    --rose-glass:#e6a48c;
    --blush-glass:#e9c4ad;
  }
  *{box-sizing:border-box;margin:0;padding:0}
  html,body{width:1200px;height:2162px;overflow:hidden;background:var(--paper)}
  body{position:relative;font-family:"Brygada 1918",Georgia,serif;color:var(--navy)}

  .brand{position:absolute;top:28px;left:0;width:1200px;text-align:center;font-size:58px;font-weight:600;color:#1f47a8;letter-spacing:1px}

  .stepper{position:absolute;left:51px;top:173px;width:624px;height:72px}
  .stepper-frame{position:absolute;left:0;top:26px;width:624px;height:46px;border:1.5px solid var(--navy);border-top:none;border-radius:0 0 24px 24px}
  .stepper-frame::after{content:"";position:absolute;right:-1.5px;top:0;width:30px;height:46px;border:1.5px solid var(--navy);border-left:none;border-radius:0 24px 24px 0}
  .step-circle{position:absolute;top:0;width:52px;height:52px;border-radius:50%;border:1.5px solid var(--navy);background:var(--paper);display:flex;align-items:center;justify-content:center;font-size:24px}
  .step-circle.is-active{background:var(--navy);color:#fff}
  .step-line{position:absolute;top:26px;height:1.5px;background:var(--navy)}
  .step-label{position:absolute;top:39px;font-size:16px;letter-spacing:.3px}

  .btn-next{position:absolute;left:1014px;width:92px;height:51px;background:var(--navy);color:#fff;font-family:"Jost",Arial,sans-serif;font-weight:300;font-size:20px;display:flex;align-items:center;justify-content:center;border-radius:3px}

  .collection-title{position:absolute;left:42px;top:288px;width:288px;height:43px;border-top:2px solid var(--gold);border-bottom:2px solid var(--gold);font-size:26px;letter-spacing:1.6px;padding-left:9px;line-height:40px}
  .intro{position:absolute;left:47px;top:351px;width:1080px;font-size:18px;line-height:23px}

  .group-title{position:absolute;left:46px;font-size:24px;font-weight:600;letter-spacing:2px}

  .product{position:absolute;width:200px;height:190px}
  .bottle{position:absolute;left:81px;top:0;width:38px;height:150px}
  .bottle-neck{position:absolute;left:13px;top:0;width:12px;height:42px;border-radius:3px 3px 0 0}
  .bottle-body{position:absolute;left:0;top:36px;width:38px;height:114px;border-radius:16px 16px 4px 4px}
  .bottle-label{position:absolute;left:5px;top:76px;width:28px;height:46px;background:rgba(255,255,255,.7);border-radius:2px}
  .badge{position:absolute;left:131px;top:-6px;width:34px;height:34px;border-radius:50%;border:1.5px solid var(--gold);color:var(--gold);font-size:7px;font-weight:600;display:flex;align-items:center;justify-content:center;letter-spacing:.3px}
  .product-name{position:absolute;left:0;top:160px;width:200px;text-align:center;font-size:12.5px;font-weight:600}
  .product-arrow{position:absolute;left:77px;top:174px}

  .product.is-selected .product-name{color:var(--gold)}
  .product.is-selected .badge{background:var(--gold);color:#fff}
  .product.is-selected .product-arrow path{stroke:var(--gold)}
  .product.is-hover > .bottle,.product.is-hover > .badge,.product.is-hover > .product-name,.product.is-hover > .product-arrow{opacity:.35}
  .hover-action{position:absolute;left:151px;width:65px;height:20px;font-family:"Jost",Arial,sans-serif;font-size:11px;display:flex;align-items:center;justify-content:center;letter-spacing:.3px}
  .hover-action.details{top:52px;background:var(--navy);color:#fff}
  .hover-action.select{top:81px;border:1px solid var(--navy);color:var(--navy);background:#fff}

  .glass-red{background:var(--red-glass)}
  .glass-white{background:var(--white-glass)}
  .glass-dark{background:#3a3a2a}
  .glass-green{background:var(--green-glass)}
  .glass-rose{background:var(--rose-glass)}
  .glass-blush{background:var(--blush-glass)}
  .glass-grey{background:#9a9aa4}
</style>
</head>
<body>

<div class="brand">Vintaro</div>

<nav class="stepper" aria-label="Redemption steps">
  <div class="stepper-frame"></div>
  <div class="step-line" style="left:61px;width:141px"></div>
  <div class="step-line" style="left:276px;width:137px"></div>
  <div class="step-line" style="left:484px;width:120px"></div>
  <div class="step-circle is-active" style="left:0">1</div>
  <div class="step-circle" style="left:213px">2</div>
  <div class="step-circle" style="left:421px">3</div>
  <span class="step-label" style="left:62px">Choose Your Gift</span>
  <span class="step-label" style="left:276px">Enter Your Address</span>
  <span class="step-label" style="left:485px">Confirm</span>
</nav>

<div class="btn-next" style="top:184px">NEXT</div>

<h1 class="collection-title">GOLD COLLECTION</h1>
<p class="intro">At Vintaro we hand select every last bottle we send. We work with some of the world’s best sommeliers to make sure you always get a great bottle. Simply choose your preferred type of wine and let us do the hard work for you.</p>

<h2 class="group-title" style="top:424px">RED</h2>

<div class="product" style="left:22px;top:498px">
  <div class="bottle" role="img" aria-label="Pinot Noir bottle photo"><div class="bottle-neck glass-red"></div><div class="bottle-body glass-red"></div><div class="bottle-label"></div></div>
  <div class="badge">GOLD</div><div class="product-name">Pinot Noir</div>
  <svg class="product-arrow" width="46" height="8"><path d="M0 4H44M40 1L44 4L40 7" stroke="#23295a" fill="none"/></svg>
</div>
<div class="product" style="left:253px;top:498px">
  <div class="bottle" role="img" aria-label="Zinfandel bottle photo"><div class="bottle-neck glass-red"></div><div class="bottle-body glass-red"></div><div class="bottle-label"></div></div>
  <div class="badge">GOLD</div><div class="product-name">Zinfandel</div>
  <svg class="product-arrow" width="46" height="8"><path d="M0 4H44M40 1L44 4L40 7" stroke="#23295a" fill="none"/></svg>
</div>
<div class="product is-selected" style="left:484px;top:498px">
  <div class="bottle" role="img" aria-label="Sangiovese bottle photo"><div class="bottle-neck glass-red"></div><div class="bottle-body glass-red"></div><div class="bottle-label"></div></div>
  <div class="badge">GOLD</div><div class="product-name">Sangiovese</div>
  <svg class="product-arrow" width="46" height="8"><path d="M0 4H44M40 1L44 4L40 7" stroke="#23295a" fill="none"/></svg>
</div>
<div class="product" style="left:716px;top:498px">
  <div class="bottle" role="img" aria-label="Cabernet Sauvignon bottle photo"><div class="bottle-neck glass-red"></div><div class="bottle-body glass-red"></div><div class="bottle-label"></div></div>
  <div class="badge">GOLD</div><div class="product-name">Cabernet Sauvignon</div>
  <svg class="product-arrow" width="46" height="8"><path d="M0 4H44M40 1L44 4L40 7" stroke="#23295a" fill="none"/></svg>
</div>
<div class="product is-hover" style="left:947px;top:498px">
  <div class="bottle" role="img" aria-label="Malbec bottle photo"><div class="bottle-neck glass-grey"></div><div class="bottle-body glass-grey"></div><div class="bottle-label"></div></div>
  <div class="badge">GOLD</div><div class="product-name">Malbec</div>
  <svg class="product-arrow" width="46" height="8"><path d="M0 4H44M40 1L44 4L40 7" stroke="#23295a" fill="none"/></svg>
  <div class="hover-action details">DETAILS</div>
  <div class="hover-action select">SELECT</div>
</div>

<div class="product" style="left:22px;top:747px">
  <div class="bottle" role="img" aria-label="Grenache bottle photo"><div class="bottle-neck glass-red"></div><div class="bottle-body glass-red"></div><div class="bottle-label"></div></div>
  <div class="badge">GOLD</div><div class="product-name">Grenache</div>
  <svg class="product-arrow" width="46" height="8"><path d="M0 4H44M40 1L44 4L40 7" stroke="#23295a" fill="none"/></svg>
</div>
<div class="product" style="left:253px;top:747px">
  <div class="bottle" role="img" aria-label="Syrah bottle photo"><div class="bottle-neck glass-red"></div><div class="bottle-body glass-red"></div><div class="bottle-label"></div></div>
  <div class="badge">GOLD</div><div class="product-name">Syrah</div>
  <svg class="product-arrow" width="46" height="8"><path d="M0 4H44M40 1L44 4L40 7" stroke="#23295a" fill="none"/></svg>
</div>
<div class="product" style="left:484px;top:747px">
  <div class="bottle" role="img" aria-label="Red Blend bottle photo"><div class="bottle-neck glass-red"></div><div class="bottle-body glass-red"></div><div class="bottle-label"></div></div>
  <div class="badge">GOLD</div><div class="product-name">Red Blend</div>
  <svg class="product-arrow" width="46" height="8"><path d="M0 4H44M40 1L44 4L40 7" stroke="#23295a" fill="none"/></svg>
</div>

<h2 class="group-title" style="top:980px">WHITE</h2>

<div class="product" style="left:22px;top:1056px">
  <div class="bottle" role="img" aria-label="Chardonnay bottle photo"><div class="bottle-neck glass-white"></div><div class="bottle-body glass-white"></div><div class="bottle-label"></div></div>
  <div class="badge">GOLD</div><div class="product-name">Chardonnay</div>
  <svg class="product-arrow" width="46" height="8"><path d="M0 4H44M40 1L44 4L40 7" stroke="#23295a" fill="none"/></svg>
</div>
<div class="product" style="left:253px;top:1056px">
  <div class="bottle" role="img" aria-label="Pinot Grigio bottle photo"><div class="bottle-neck glass-dark"></div><div class="bottle-body glass-dark"></div><div class="bottle-label"></div></div>
  <div class="badge">GOLD</div><div class="product-name">Pinot Grigio</div>
  <svg class="product-arrow" width="46" height="8"><path d="M0 4H44M40 1L44 4L40 7" stroke="#23295a" fill="none"/></svg>
</div>
<div class="product" style="left:484px;top:1056px">
  <div class="bottle" role="img" aria-label="Sauvignon Blanc bottle photo"><div class="bottle-neck glass-white"></div><div class="bottle-body glass-white"></div><div class="bottle-label"></div></div>
  <div class="badge">GOLD</div><div class="product-name">Sauvignon Blanc</div>
  <svg class="product-arrow" width="46" height="8"><path d="M0 4H44M40 1L44 4L40 7" stroke="#23295a" fill="none"/></svg>
</div>
<div class="product" style="left:716px;top:1056px">
  <div class="bottle" role="img" aria-label="Riesling bottle photo"><div class="bottle-neck glass-dark"></div><div class="bottle-body glass-dark"></div><div class="bottle-label"></div></div>
  <div class="badge">GOLD</div><div class="product-name">Reisling</div>
  <svg class="product-arrow" width="46" height="8"><path d="M0 4H44M40 1L44 4L40 7" stroke="#23295a" fill="none"/></svg>
</div>

<h2 class="group-title" style="top:1288px">SPARKLING</h2>

<div class="product" style="left:22px;top:1366px">
  <div class="bottle" role="img" aria-label="Non-vintage champagne bottle photo"><div class="bottle-neck glass-green"></div><div class="bottle-body glass-green"></div><div class="bottle-label"></div></div>
  <div class="badge">GOLD</div><div class="product-name">Champagne Non-Vintage</div>
  <svg class="product-arrow" width="46" height="8"><path d="M0 4H44M40 1L44 4L40 7" stroke="#23295a" fill="none"/></svg>
</div>
<div class="product" style="left:253px;top:1366px">
  <div class="bottle" role="img" aria-label="Rosé champagne bottle photo"><div class="bottle-neck glass-rose"></div><div class="bottle-body glass-rose"></div><div class="bottle-label"></div></div>
  <div class="badge">GOLD</div><div class="product-name">Rosé Champagne</div>
  <svg class="product-arrow" width="46" height="8"><path d="M0 4H44M40 1L44 4L40 7" stroke="#23295a" fill="none"/></svg>
</div>
<div class="product" style="left:484px;top:1366px">
  <div class="bottle" role="img" aria-label="Prosecco bottle photo"><div class="bottle-neck glass-white"></div><div class="bottle-body glass-white"></div><div class="bottle-label"></div></div>
  <div class="badge">GOLD</div><div class="product-name">Prosecco</div>
  <svg class="product-arrow" width="46" height="8"><path d="M0 4H44M40 1L44 4L40 7" stroke="#23295a" fill="none"/></svg>
</div>

<h2 class="group-title" style="top:1595px">ROSE</h2>

<div class="product" style="left:22px;top:1674px">
  <div class="bottle" role="img" aria-label="Rosé bottle photo"><div class="bottle-neck glass-grey"></div><div class="bottle-body glass-blush"></div><div class="bottle-label"></div></div>
  <div class="badge">GOLD</div><div class="product-name">Rosé</div>
  <svg class="product-arrow" width="46" height="8"><path d="M0 4H44M40 1L44 4L40 7" stroke="#23295a" fill="none"/></svg>
</div>

<div class="btn-next" style="top:1946px">NEXT</div>

</body>
</html>
```